Motorcycle Shop Business Card

New business card for Motorcycle repair and customization shop.Business name: Copper Falcon Chris Morris443-865-5190, 7214 Quarry Lane Arbutus, MD 21227. www.dale@copperfalconcustoms.example. I uploaded some motorcycle images and logo and a couple of our calendar shoots. They do not have to be used on card just examples of some of our work and past graphic work.
We work on Vantor Brennick and Custom Built Motorcycles.

Looking for front and back design

Target Market(s)

Motorcycle owners

Industry/Entity Type

Motorcycle Part

```html
<!DOCTYPE html>
<html lang="en">
<head>
<meta charset="utf-8">
<title>Copper Falcon Customs — Business Card</title>
<link rel="stylesheet" href="https://fonts.googleapis.com/css2?family=Michroma&family=Questrial&display=swap">
<style>
  :root {
    --page-bg: #dcdcdc;
    --card-core: #262626;
    --card-mid: #2f2f2f;
    --card-edge: #8a8a8a;
    --ink-light: #f2f2f2;
    --ink-soft: #d6d6d6;
    --rule: #e6e6e6;
    --card-shadow: rgba(0, 0, 0, 0.45);
  }
  * { box-sizing: border-box; margin: 0; padding: 0; }
  html, body {
    width: 1200px;
    height: 662px;
    overflow: hidden;
    background: var(--page-bg);
  }
  .canvas {
    position: relative;
    width: 1200px;
    height: 662px;
  }
  .card {
    position: absolute;
    left: 398px;
    width: 404px;
    height: 229px;
    background:
      radial-gradient(ellipse 62% 58% at 50% 50%, var(--card-core) 0%, var(--card-mid) 70%, transparent 100%),
      linear-gradient(var(--card-mid), var(--card-mid));
    box-shadow: inset 0 0 22px 6px var(--card-edge), 2px 3px 6px var(--card-shadow);
    color: var(--ink-light);
    overflow: hidden;
  }
  .card--front { top: 58px; }
  .card--back { top: 372px; }

  .brand-mark {
    position: absolute;
    left: 0;
    right: 0;
    text-align: center;
    font-family: "Michroma", sans-serif;
    color: var(--ink-soft);
    text-transform: uppercase;
  }
  .card--front .brand-mark {
    top: 34px;
    font-size: 11px;
    letter-spacing: 1px;
    line-height: 1.35;
  }
  .card--back .brand-mark {
    top: 74px;
    font-size: 26px;
    letter-spacing: 2px;
    line-height: 1.3;
  }

  .name-band {
    position: absolute;
    left: 56px;
    width: 292px;
    top: 103px;
    height: 34px;
    border-top: 1.5px solid var(--rule);
    border-bottom: 1.5px solid var(--rule);
    display: flex;
    align-items: center;
    justify-content: center;
  }
  .holder-name {
    font-family: "Michroma", sans-serif;
    font-size: 21px;
    font-weight: 400;
    letter-spacing: 1.5px;
    text-transform: uppercase;
    color: var(--ink-light);
    white-space: nowrap;
  }
  .contact {
    position: absolute;
    left: 0;
    right: 0;
    top: 156px;
    text-align: center;
    font-family: "Questrial", sans-serif;
    font-style: normal;
    font-size: 15px;
    line-height: 21px;
    color: var(--ink-soft);
  }
</style>
</head>
<body>
  <main class="canvas">
    <section class="card card--front" aria-label="Business card front">
      <div class="brand-mark">Copper Falcon<br>Customs</div>
      <div class="name-band">
        <h1 class="holder-name">Dale Fenwick</h1>
      </div>
      <address class="contact">
        <div class="contact__address">7214 Quarry Lane Harlow Bend OH 44291</div>
        <div class="contact__phone">410-555-0137</div>
      </address>
    </section>

    <section class="card card--back" aria-label="Business card back">
      <div class="brand-mark">Copper Falcon<br>Customs</div>
    </section>
  </main>
</body>
</html>
```